Ridgeline Outfitters Business Cards

Recently had a logo done with Artfolio and now looking for a business card to go along with it.

Target Market(s)

Ridgeline Outfitters is a weapons dealer. My market will be primarily men, hunting, shooting type.

Industry/Entity Type

Business

Contact Information for Business Card

I selected double sided, but this is not required, single or double is going to be fine. I picture the logo on one side, or perhaps just the circle which contains "RO" with the remaining info on the other side.

Font styles to use
Sans Serif

Requirements
Must have
• My name: Milo Brandt
• Title: Owner
• tel: 612-555-0187
• web: www.ridgelineoutfittersmn.example
Nice to have
• I like the concept of a black business card. I would like to keep the colors monotone, black, grey, white or red. Red is acceptable because it is in the logo. I have also seen cards that are matte black with shiny black as well, perhaps for the logo (or circle RO) part of the logo.
• I will upload a couple of the logos for use, and also an example I just found of the black on black. and some others that have a nice contrast.
Should not have
• lots of colors are not wanted.

```html
<!DOCTYPE html>
<html lang="en">
<head>
<meta charset="utf-8">
<title>Ridgeline Outfitters — Business Cards</title>
<link href="https://fonts.googleapis.com/css2?family=Roboto+Slab:wght@400;700&display=swap" rel="stylesheet">
<style>
  :root {
    --backdrop: #5b6468;
    --card-edge: #050505;
    --card-face: #1b1919;
    --accent-red: #e3242b;
    --mid-grey: #6f6f6f;
    --text-white: #f2f2f2;
    --text-soft: #cfcfcf;
  }
  * { box-sizing: border-box; margin: 0; padding: 0; }
  html, body { width: 1200px; height: 1200px; overflow: hidden; }
  body {
    background: var(--backdrop);
    font-family: "Roboto Slab", Georgia, serif;
    position: relative;
  }
  .card {
    position: absolute;
    left: 170px;
    width: 860px;
    height: 491px;
    background: var(--card-edge);
    border-radius: 30px;
    padding: 22px;
  }
  .card--front { top: 92px; }
  .card--back { top: 617px; }
  .card__face {
    position: relative;
    width: 100%;
    height: 100%;
    border-radius: 14px;
    background: var(--card-face);
    overflow: hidden;
  }
  .brand {
    position: absolute;
    display: flex;
    align-items: center;
    gap: 14px;
  }
  .brand__dot {
    width: 26px;
    height: 26px;
    border-radius: 50%;
    background: var(--accent-red);
    flex: none;
  }
  .brand__name {
    color: var(--text-white);
    font-weight: 700;
    text-transform: uppercase;
    letter-spacing: 1px;
    line-height: 1.1;
  }
  .card--front .brand { left: 60px; top: 205px; }
  .card--front .brand__name { font-size: 22px; }
  .card--back .brand { left: 50%; top: 50%; transform: translate(-50%, -50%); }
  .card--back .brand__name { font-size: 34px; }

  .contact {
    position: absolute;
    left: 400px;
    top: 120px;
  }
  .contact__name {
    font-size: 44px;
    font-weight: 700;
    text-transform: uppercase;
    letter-spacing: 1px;
    line-height: 1;
  }
  .contact__first { color: var(--accent-red); }
  .contact__last { color: var(--mid-grey); }
  .contact__title {
    color: var(--text-white);
    font-size: 34px;
    font-weight: 400;
    letter-spacing: 2px;
    margin-top: 4px;
  }
  .contact__list { list-style: none; margin-top: 18px; }
  .contact__item {
    display: flex;
    align-items: center;
    gap: 12px;
    color: var(--text-soft);
    font-size: 17px;
    margin-bottom: 8px;
  }
  .contact__icon { width: 20px; height: 20px; flex: none; }
</style>
</head>
<body>
  <section class="card card--front">
    <div class="card__face" role="img" aria-label="Dark geometric maze-line pattern across the card face">
      <div class="brand">
        <span class="brand__dot"></span>
        <span class="brand__name">Ridgeline<br>Outfitters</span>
      </div>
      <div class="contact">
        <h1 class="contact__name"><span class="contact__first">Milo</span> <span class="contact__last">Brandt</span></h1>
        <p class="contact__title">OWNER</p>
        <ul class="contact__list">
          <li class="contact__item">
            <svg class="contact__icon" viewBox="0 0 20 20" aria-hidden="true"><circle cx="10" cy="10" r="9" fill="none" stroke="#cfcfcf" stroke-width="1.3"/><path d="M7 5.5l1.6 2.3-1 1.2a6 6 0 0 0 2.6 2.6l1.2-1 2.3 1.6-.9 1.6c-3.6-.3-6.5-3.2-6.8-6.8z" fill="#cfcfcf"/></svg>
            612-555-0187
          </li>
          <li class="contact__item">
            <svg class="contact__icon" viewBox="0 0 20 20" aria-hidden="true"><circle cx="10" cy="10" r="9" fill="none" stroke="#cfcfcf" stroke-width="1.3"/><circle cx="10" cy="10" r="4.5" fill="none" stroke="#cfcfcf" stroke-width="1.2"/><path d="M5.5 10h9M10 5.5c1.6 1.3 1.6 7.7 0 9M10 5.5c-1.6 1.3-1.6 7.7 0 9" fill="none" stroke="#cfcfcf" stroke-width="1"/></svg>
            www.ridgelineoutfittersmn.example
          </li>
        </ul>
      </div>
    </div>
  </section>

  <section class="card card--back">
    <div class="card__face" role="img" aria-label="Dark geometric maze-line pattern across the card face">
      <div class="brand">
        <span class="brand__dot"></span>
        <span class="brand__name">Ridgeline Outfitters</span>
      </div>
    </div>
  </section>
</body>
</html>
```